Menu Cards - Bar & Restaurant

We're a casual college sports bar in Madison, WI. We're looking for simple & creative design for menu cards that are double sided. The first card is to identify our wing sauces on the front side with our tap list on the back. The second card is for our taco night and again our tap list on the back. The font used in our logo is Air Conditioner, but I don't want this to be limiting.
Target Market(s)
18-25 college kids
Industry/Entity Type
College

```html
<!DOCTYPE html>
<html lang="en">
<head>
<meta charset="utf-8">
<title>Wing Sauces Menu Card</title>
<link href="https://fonts.googleapis.com/css2?family=Bungee+Inline&family=Raleway:wght@300;400&display=swap" rel="stylesheet">
<style>
  :root {
    --board: #1f1f1f;
    --board-edge: #161616;
    --chalk: #e9e9e9;
    --chalk-soft: #bdbdbd;
    --mild: #8cc63f;
    --medium: #f7941d;
    --hot: #e8332f;
    --title: #e8332f;
  }
  html, body {
    margin: 0;
    padding: 0;
    width: 1200px;
    height: 929px;
    overflow: hidden;
    background: var(--board-edge);
  }
  .menu-card {
    position: relative;
    width: 1200px;
    height: 929px;
    background: radial-gradient(ellipse at 50% 45%, #2a2a2a 0%, var(--board) 60%, var(--board-edge) 100%);
    font-family: "Raleway", sans-serif;
    color: var(--chalk-soft);
    overflow: hidden;
  }
  .chalk-frame {
    position: absolute;
    inset: 0;
  }
  .card-title {
    position: absolute;
    left: 0;
    width: 1200px;
    top: 22px;
    margin: 0;
    text-align: center;
    font-family: "Bungee Inline", sans-serif;
    font-weight: 400;
    font-size: 84px;
    letter-spacing: 10px;
    line-height: 1;
    color: var(--title);
  }
  .sauce-list {
    position: absolute;
    left: 500px;
    top: 148px;
    margin: 0;
    padding: 0;
    list-style: none;
    font-weight: 300;
    font-size: 44px;
    line-height: 60.2px;
    color: var(--chalk-soft);
  }
  .heat-label {
    position: absolute;
    box-sizing: border-box;
    border: 3px dashed var(--chalk);
    outline: 2px solid rgba(233,233,233,0.5);
    outline-offset: 4px;
    text-align: center;
    font-weight: 300;
    font-size: 58px;
    line-height: 66px;
    height: 72px;
  }
  .heat-label.mild { left: 262px; top: 224px; width: 180px; color: var(--mild); }
  .heat-label.medium { left: 143px; top: 440px; width: 304px; color: var(--medium); }
  .heat-label.hot { left: 283px; top: 694px; width: 164px; color: var(--hot); }
  .heat-note {
    position: absolute;
    font-weight: 300;
    font-size: 30px;
    color: var(--chalk-soft);
    text-align: right;
    right: 757px;
    white-space: nowrap;
  }
  .heat-note.mild-note { top: 344px; }
  .heat-note.medium-note { top: 535px; }
  .heat-note.hot-note { top: 618px; }
  .bar-badge {
    position: absolute;
    left: 863px;
    top: 193px;
    width: 240px;
    height: 240px;
    border-radius: 50%;
    background: var(--hot);
    display: flex;
    align-items: center;
    justify-content: center;
  }
  .bar-name {
    font-family: "Raleway", sans-serif;
    font-weight: 400;
    font-size: 52px;
    color: var(--chalk);
    letter-spacing: 2px;
  }
</style>
</head>
<body>
<main class="menu-card">
  <svg class="chalk-frame" width="1200" height="929" viewBox="0 0 1200 929" aria-hidden="true">
    <g fill="none" stroke="var(--chalk)" stroke-linecap="round">
      <!-- outer border, broken at title -->
      <path d="M270 40 H40 V890 H1160 V40 H930" stroke-width="5"/>
      <path d="M280 52 H52 V878 H1148 V52 H920" stroke-width="2" opacity="0.7"/>
      <!-- corner notches -->
      <path d="M40 70 H70 V40" stroke-width="3"/>
      <path d="M1160 70 H1130 V40" stroke-width="3"/>
      <path d="M40 860 H70 V890" stroke-width="3"/>
      <path d="M1160 860 H1130 V890" stroke-width="3"/>
    </g>
    <!-- heat scale -->
    <g stroke="var(--chalk)" stroke-width="3">
      <line x1="456" y1="175" x2="456" y2="805"/>
      <line x1="436" y1="230" x2="456" y2="230"/>
      <line x1="436" y1="290" x2="456" y2="290"/>
      <line x1="436" y1="351" x2="456" y2="351"/>
      <line x1="436" y1="411" x2="456" y2="411"/>
      <line x1="436" y1="471" x2="456" y2="471"/>
      <line x1="436" y1="531" x2="456" y2="531"/>
      <line x1="436" y1="591" x2="456" y2="591"/>
      <line x1="436" y1="652" x2="456" y2="652"/>
      <line x1="436" y1="712" x2="456" y2="712"/>
      <line x1="436" y1="772" x2="456" y2="772"/>
    </g>
    <path d="M424 190 L456 152 L488 190" fill="none" stroke="var(--mild)" stroke-width="9" stroke-linejoin="miter"/>
    <path d="M424 792 L456 830 L488 792" fill="none" stroke="var(--hot)" stroke-width="9" stroke-linejoin="miter"/>
  </svg>

  <h1 class="card-title">WING SAUCES</h1>

  <div class="heat-label mild">MILD</div>
  <div class="heat-note mild-note">(That ain't hot.)</div>
  <div class="heat-label medium">MEDIUM</div>
  <div class="heat-note medium-note">(Is it warm in here?)</div>
  <div class="heat-note hot-note">(Holy @#&amp;*!)</div>
  <div class="heat-label hot">HOT</div>

  <ul class="sauce-list">
    <li>Chesapeake Butter</li>
    <li>Honey BBQ</li>
    <li>House</li>
    <li>Spicy Garlic</li>
    <li>Sweet Chili</li>
    <li>Jamaican Jerk</li>
    <li>Spicy Buffalo Ranch</li>
    <li>Buffalo</li>
    <li>Hot BBQ</li>
    <li>Thai Peanut</li>
    <li>Spicy Tequila Lime</li>
    <li>Thermo-Nuke</li>
  </ul>

  <div class="bar-badge"><span class="bar-name">Huddle</span></div>
</main>
</body>
</html>
```